Business Card Design

I am starting my therapy private practice. I will be an in home therapist, so I go into family's homes instead of using an office to do family/marriage therapy. Therefore, I do not have an office address. I am looking for something in the black, red, gray, and blue color scheme that appeals to both families, couples and teenagers.

Industry/Entity Type

Business

Contact Information for Business Card

Lena Brightwell, MS, MFT Intern
Marriage and Family Therapy
In Home Therapist
617-482-5190
Lena@LenaBrightwell-example.com

```html
<!DOCTYPE html>
<html lang="en">
<head>
<meta charset="utf-8">
<title>Lena Brightwell – Business Card</title>
<link rel="stylesheet" href="https://fonts.googleapis.com/css2?family=Dancing+Script:wght@400&family=Parisienne&family=Cormorant+Garamond:wght@500&family=Open+Sans:wght@400&display=swap">
<style>
  :root {
    --backdrop: #d4d4d4;
    --card-white: #ffffff;
    --frame-dark: #9a9a9a;
    --frame-bottom: #b5b5b5;
    --brand-red: #c8161d;
    --brand-red-deep: #8e0f12;
    --name-silver: #7d7d7d;
    --ink: #3a3a3a;
    --ghost: #efefef;
  }
  html, body {
    margin: 0;
    width: 1200px;
    height: 900px;
    overflow: hidden;
    background: var(--backdrop);
  }
  .business-card {
    position: absolute;
    left: 120px;
    top: 180px;
    width: 960px;
    height: 540px;
    box-sizing: border-box;
    background: var(--card-white);
    border-radius: 44px;
    padding: 14px;
  }
  .card-frame {
    position: relative;
    width: 100%;
    height: 100%;
    box-sizing: border-box;
    border-radius: 34px;
    border: 14px solid var(--frame-dark);
    border-bottom-color: var(--frame-bottom);
    background: var(--card-white);
    overflow: hidden;
  }
  .family-tree-art {
    position: absolute;
    left: 14px;
    top: 6px;
    width: 256px;
    height: 290px;
    border-radius: 120px 120px 8px 8px;
    background: radial-gradient(ellipse at 50% 35%, var(--brand-red) 0%, var(--brand-red-deep) 100%);
  }
  .family-tree-ghost {
    position: absolute;
    right: 10px;
    top: 200px;
    width: 250px;
    height: 300px;
    border-radius: 120px 120px 8px 8px;
    background: var(--ghost);
  }
  .identity {
    position: absolute;
    left: 280px;
    top: 64px;
  }
  .identity .role {
    margin: 0 0 0 90px;
    font-family: "Dancing Script", cursive;
    font-size: 22px;
    line-height: 1.2;
    color: var(--brand-red);
  }
  .identity .name {
    margin: 0;
    font-family: "Parisienne", cursive;
    font-weight: 400;
    font-size: 64px;
    line-height: 1.1;
    color: var(--name-silver);
    white-space: nowrap;
  }
  .identity .credentials {
    margin: 10px 0 0 6px;
    font-family: "Cormorant Garamond", serif;
    font-weight: 500;
    font-size: 19px;
    color: var(--brand-red);
  }
  .contact {
    position: absolute;
    left: 36px;
    top: 360px;
    margin: 0;
    padding: 0;
    list-style: none;
    font-family: "Open Sans", sans-serif;
    font-size: 27px;
    line-height: 1;
    color: var(--ink);
  }
  .contact li {
    display: flex;
    align-items: center;
    gap: 10px;
    height: 40px;
  }
  .contact svg { width: 26px; height: 22px; flex: none; }
</style>
</head>
<body>
  <div class="business-card">
    <div class="card-frame">
      <div class="family-tree-ghost" role="img" aria-label="Faint background illustration of a family tree with parents and child"></div>
      <div class="family-tree-art" role="img" aria-label="Red illustration of a heart-shaped tree with two parents and a child beneath"></div>

      <div class="identity">
        <p class="role">In Home Therapist</p>
        <h1 class="name">Lena Brightwell</h1>
        <p class="credentials">MS, MFT Intern Marriage and Family Therapy</p>
      </div>

      <ul class="contact">
        <li>
          <svg viewBox="0 0 24 24" aria-hidden="true"><path fill="var(--brand-red)" d="M6.6 10.8a15.1 15.1 0 0 0 6.6 6.6l2.2-2.2a1 1 0 0 1 1-.25 11.4 11.4 0 0 0 3.6.57 1 1 0 0 1 1 1V20a1 1 0 0 1-1 1A17 17 0 0 1 3 4a1 1 0 0 1 1-1h3.5a1 1 0 0 1 1 1 11.4 11.4 0 0 0 .57 3.6 1 1 0 0 1-.25 1z"/></svg>
          <span>617-482-5190</span>
        </li>
        <li>
          <svg viewBox="0 0 26 20" aria-hidden="true"><rect x="1" y="2" width="24" height="16" rx="1.5" fill="var(--brand-red)"/><path d="M2 3l11 8 11-8" fill="none" stroke="#fff" stroke-width="1.6"/></svg>
          <span>Lena@LenaBrightwell-example.com</span>
        </li>
      </ul>
    </div>
  </div>
</body>
</html>
```